Letter Head Design

I need a letter head design based on my company logo that I attached.
Include phone number: (403)582-3140
Address: 417 Brindlewood Avenue NE, Calgary, Alberta, Canada, T3M 4K8

Industry/Entity Type

It Company

```html
<!DOCTYPE html>
<html lang="en">
<head>
<meta charset="utf-8">
<title>Lumenroom Interiors Corp. Letterhead</title>
<link rel="stylesheet" href="https://fonts.googleapis.com/css2?family=Marcellus&display=swap">
<style>
  :root {
    --canvas: #ffffff;
    --paper: #f8faf8;
    --ink: #111111;
    --brand-blue: #1560b8;
    --brand-blue-deep: #0b4a9c;
    --brand-green: #5cb21e;
    --on-band: #ffffff;
  }
  * { margin: 0; padding: 0; box-sizing: border-box; }
  html, body {
    width: 1200px;
    height: 1000px;
    overflow: hidden;
    background: var(--canvas);
  }
  .letterhead {
    position: absolute;
    left: 252px;
    top: 0;
    width: 738px;
    height: 981px;
    background: var(--paper);
    font-family: "Marcellus", "Palatino Linotype", serif;
  }
  .brand {
    position: absolute;
    left: 16px;
    top: 2px;
    display: flex;
    flex-direction: column;
    align-items: flex-start;
    gap: 6px;
  }
  .brand-square {
    width: 70px;
    height: 70px;
    background: var(--brand-green);
    border-radius: 4px;
  }
  .brand-name {
    font-size: 20px;
    color: var(--brand-blue);
    line-height: 1;
    white-space: nowrap;
  }
  .contact {
    position: absolute;
    right: 16px;
    top: 2px;
    list-style: none;
    font-size: 19px;
    color: var(--ink);
    line-height: 23px;
    white-space: nowrap;
  }
  .footer-band {
    position: absolute;
    left: 0;
    bottom: 0;
    width: 738px;
    height: 40px;
  }
  .footer-name {
    position: absolute;
    right: 14px;
    bottom: 9px;
    display: flex;
    align-items: center;
    gap: 10px;
    font-size: 15px;
    color: var(--on-band);
  }
  .footer-square {
    width: 44px;
    height: 24px;
    border: 2px solid var(--on-band);
    border-radius: 2px;
  }
</style>
</head>
<body>
  <main class="letterhead">
    <header>
      <div class="brand">
        <span class="brand-square"></span>
        <span class="brand-name">Lumenroom Interiors</span>
      </div>
      <ul class="contact">
        <li>417 Brindlewood Avenue NE</li>
        <li>Calgary, Alberta, Canada T3M 4K8</li>
        <li>(403)582-3140</li>
        <li>www.lumenroom.ca</li>
      </ul>
    </header>

    <footer>
      <svg class="footer-band" viewBox="0 0 738 40" aria-hidden="true">
        <defs>
          <linearGradient id="bandFill" x1="0" y1="0" x2="1" y2="1">
            <stop offset="0" stop-color="#2f7fd6"/>
            <stop offset="1" stop-color="#0b4a9c"/>
          </linearGradient>
        </defs>
        <polygon points="478,38 546,0 736,0 736,38" fill="url(#bandFill)"/>
        <rect x="1" y="36" width="735" height="3" fill="var(--brand-blue-deep)"/>
      </svg>
      <div class="footer-name">
        <span class="footer-square"></span>
        <span>Lumenroom</span>
      </div>
    </footer>
  </main>
</body>
</html>
```